Wag Without Worry Business cards

Design a cool, modern business card for my bully breed rescue.

Contact Information for Business Card

Mirela
512-384-2076 Mirela@WagWithoutWorry.net WagWithoutWorry.net

Font styles to use
Serif
Sans Serif

Colors

Designer to choose colors to be used in the design.

Requirements
Must have
• logo and info. Color
Nice to have
• Foil. Maybe some paw prints on the back or some kind of dog illustration.

```html
<!DOCTYPE html>
<html lang="en">
<head>
<meta charset="utf-8">
<title>Wag Without Worry – Business Cards</title>
<link rel="stylesheet" href="https://fonts.googleapis.com/css2?family=Cinzel:wght@700&family=Arimo:wght@400&display=swap">
<style>
  :root {
    --stage: #e6e6e6;
    --paper: #f4f4f4;
    --ink: #111111;
    --red: #e32636;
    --brown: #3b1d12;
    --gold: #e5b920;
    --white: #ffffff;
  }
  * { margin: 0; padding: 0; box-sizing: border-box; }
  html, body {
    width: 1200px;
    height: 864px;
    overflow: hidden;
    background: var(--stage);
  }
  .sheet {
    position: relative;
    width: 1200px;
    height: 864px;
  }
  .card {
    position: absolute;
    width: 620px;
    height: 354px;
    background: var(--paper);
    box-shadow: 0 6px 18px rgba(0,0,0,0.18);
    overflow: hidden;
  }
  .card-back { left: 530px; top: 50px; }
  .card-front { left: 50px; top: 460px; }
  .card svg.art {
    position: absolute;
    inset: 0;
    width: 100%;
    height: 100%;
  }
  .brand-name {
    position: absolute;
    font-family: "Cinzel", Georgia, serif;
    font-weight: 700;
    color: var(--ink);
    text-align: center;
    line-height: 1.05;
    text-transform: uppercase;
  }
  .card-back .brand-name {
    left: 150px;
    width: 320px;
    top: 128px;
    font-size: 34px;
  }
  .card-front .brand-name {
    left: 40px;
    width: 280px;
    top: 46px;
    font-size: 30px;
  }
  .person-name {
    position: absolute;
    right: 56px;
    top: 138px;
    font-family: "Cinzel", Georgia, serif;
    font-weight: 700;
    font-size: 28px;
    letter-spacing: 1px;
    color: var(--ink);
  }
  .contact-list {
    position: absolute;
    right: 30px;
    top: 258px;
    list-style: none;
    font-family: "Arimo", Arial, sans-serif;
    font-size: 19px;
    color: var(--white);
  }
  .contact-list li {
    display: flex;
    justify-content: flex-end;
    align-items: center;
    gap: 12px;
    height: 27px;
  }
  .contact-icon {
    width: 17px;
    height: 17px;
    flex: none;
  }
</style>
</head>
<body>
<main class="sheet">

  <!-- Back of card -->
  <section class="card card-back">
    <svg class="art" viewBox="0 0 620 354" aria-hidden="true">
      <line x1="0" y1="62" x2="170" y2="62" stroke="var(--brown)" stroke-width="3"/>
      <line x1="0" y1="292" x2="170" y2="292" stroke="var(--brown)" stroke-width="3"/>
      <path d="M0,70 L165,70 Q118,177 165,284 L0,284 Z" fill="var(--red)"/>
      <line x1="450" y1="62" x2="620" y2="62" stroke="var(--brown)" stroke-width="3"/>
      <line x1="450" y1="292" x2="620" y2="292" stroke="var(--brown)" stroke-width="3"/>
      <path d="M620,70 L455,70 Q502,177 455,284 L620,284 Z" fill="var(--red)"/>
    </svg>
    <div class="brand-name">Wag Without<br>Worry</div>
  </section>

  <!-- Front of card -->
  <section class="card card-front">
    <svg class="art" viewBox="0 0 620 354" aria-hidden="true">
      <path class="swoosh-red" d="M0,160 C70,195 170,220 300,222 C180,222 80,208 0,188 Z" fill="var(--red)"/>
      <path class="panel-black" d="M0,196 C110,226 200,240 320,236 C430,232 520,222 620,226 L620,354 L0,354 Z" fill="var(--ink)"/>
      <path class="swoosh-white" d="M80,232 C190,262 300,254 410,236 C490,224 560,226 600,234 C520,230 440,240 360,254 C260,270 170,262 80,232 Z" fill="var(--white)"/>
    </svg>

    <div class="brand-name">Wag Without<br>Worry</div>
    <div class="person-name">MIRELA</div>

    <ul class="contact-list">
      <li>512-384-2076
        <svg class="contact-icon" viewBox="0 0 17 17" aria-label="Phone">
          <rect width="17" height="17" fill="var(--gold)"/>
          <path d="M5,3.5 L7,3.5 L7.6,6.2 L6.4,7.2 C7,8.6 8.4,10 9.8,10.6 L10.8,9.4 L13.5,10 L13.5,12 C13.5,12.8 12.8,13.5 12,13.5 C7.6,13.2 3.8,9.4 3.5,5 C3.5,4.2 4.2,3.5 5,3.5 Z" fill="var(--ink)"/>
        </svg>
      </li>
      <li>Mirela@WagWithoutWorry.net
        <svg class="contact-icon" viewBox="0 0 17 17" aria-label="Email">
          <rect width="17" height="17" fill="var(--gold)"/>
          <rect x="3" y="5" width="11" height="7.5" fill="none" stroke="var(--ink)" stroke-width="1.2"/>
          <path d="M3,5 L8.5,9.2 L14,5" fill="none" stroke="var(--ink)" stroke-width="1.2"/>
        </svg>
      </li>
      <li>WagWithoutWorry.net
        <svg class="contact-icon" viewBox="0 0 17 17" aria-label="Website">
          <rect width="17" height="17" fill="var(--gold)"/>
          <circle cx="8.5" cy="8.5" r="5" fill="none" stroke="var(--ink)" stroke-width="1.1"/>
          <ellipse cx="8.5" cy="8.5" rx="2.2" ry="5" fill="none" stroke="var(--ink)" stroke-width="1"/>
          <line x1="3.5" y1="8.5" x2="13.5" y2="8.5" stroke="var(--ink)" stroke-width="1"/>
        </svg>
      </li>
    </ul>
  </section>

</main>
</body>
</html>
```